Brightlane Pixel Collective Website

I need my website redesigned to look very modern with the latest services. Check out my old website for information: www.brightlanepixelcollective.com

You can use the same site menu links

It doesn't need to have the Recent News section

Please use the yellow, black and grey color scheme
Updates

This project is now payment guaranteed. Lets see what everyone can do!

Target Market(s)

25-50 years in range. Small Business Owners

Industry/Entity Type

Group

Requirements
Must have
• Logo and similar color scheme to current website
• Modern, Modern, Modern! I want a very fresh and modern look
Should not have
• Boring Look

```html
<!DOCTYPE html>
<html lang="en">
<head>
<meta charset="utf-8">
<title>Brightlane Pixel Collective</title>
<link href="https://fonts.googleapis.com/css2?family=Oswald:wght@400;500;600&family=Open+Sans:wght@400;600;700&display=swap" rel="stylesheet">
<style>
:root{
  --yellow:#fbb829;
  --yellow-deep:#f4a60d;
  --black:#000;
  --ink:#1a1a1a;
  --grey-dark:#2b2b2b;
  --grey-footer:#3d3d3d;
  --grey-mid:#6b6b6b;
  --grey-light:#d8d8d8;
  --white:#fff;
  --text-light:#dcdcdc;
}
*{box-sizing:border-box;margin:0;padding:0}
html,body{width:790px;height:1200px;overflow:hidden;background:var(--black)}
body{font-family:'Open Sans',Arial,sans-serif;position:relative}
.abs{position:absolute}
.heading{font-family:'Oswald',Arial,sans-serif;font-weight:500;text-transform:uppercase;letter-spacing:-.2px;white-space:nowrap}

/* header */
.site-header{position:absolute;left:0;top:0;width:790px;height:98px;background:linear-gradient(#ffffff,#d2d2d2);border-top:5px solid #111}
.brand{position:absolute;left:100px;top:24px;width:160px;display:flex;align-items:center;gap:8px}
.brand-mark{width:20px;height:20px;background:var(--yellow);flex:none}
.brand-name{font-family:'Open Sans',sans-serif;font-weight:600;font-size:13px;line-height:16px;color:#555}
.phones{position:absolute;right:105px;top:18px;font-family:'Oswald',sans-serif;font-size:15px;color:#333;letter-spacing:-.3px}
.phones b{font-weight:600;color:#222}
.phones span{color:#777;margin-right:12px}
.main-nav{position:absolute;left:283px;top:56px;width:507px;height:31px;background:linear-gradient(#2a2a2a,#050505);display:flex}
.nav-home{width:50px;height:31px;background:var(--yellow);clip-path:polygon(14% 0,100% 0,100% 100%,0 100%);display:flex;align-items:center;justify-content:center;padding-left:6px}
.main-nav a{color:var(--white);font-size:9px;font-weight:600;text-decoration:none;text-transform:uppercase;padding:0 10px;line-height:31px;border-right:1px solid #444}
.main-nav a:last-child{border-right:none}

/* hero */
.hero{position:absolute;left:0;top:98px;width:790px;height:254px;background:linear-gradient(100deg,#8a7f6b 0%,#a8a292 30%,#c9c8bc 60%,#e1e1da 100%)}
.slider-dots{position:absolute;left:378px;top:325px;display:flex;gap:4px}
.slider-dots i{width:8px;height:8px;border-radius:50%;background:#ddd}
.slider-dots i.on{background:var(--yellow)}

/* services */
.services{position:absolute;left:0;top:352px;width:790px;height:257px;background:linear-gradient(var(--yellow-deep),var(--yellow) 20px)}
.service{position:absolute;top:26px;width:151px;text-align:center}
.service + .service{border-left:1px dashed rgba(0,0,0,.15)}
.svc-icon{width:76px;height:76px;border-radius:50%;background:var(--grey-dark);margin:0 auto;display:flex;align-items:center;justify-content:center}
.svc-icon.active{background:var(--black);box-shadow:0 0 0 2px var(--yellow),0 0 0 3px var(--black)}
.service h3{font-size:15.5px;color:var(--ink);margin-top:14px;line-height:22px;font-weight:500;letter-spacing:-.5px}
.service p{font-size:8.6px;line-height:12px;color:#3a2a00;margin:4px 6px 0;height:62px}
.btn-dark{display:inline-block;background:var(--black);color:var(--white);font-size:8.5px;font-weight:600;padding:0 8px;line-height:20px;margin-top:10px}
.btn-yellow{display:inline-block;background:var(--yellow);color:var(--ink);font-size:8.5px;font-weight:600;padding:0 8px;line-height:19px;text-transform:uppercase}

/* welcome */
.welcome-logo{left:101px;top:633px;width:252px;height:127px;background:var(--white);display:flex;align-items:center;justify-content:center;gap:10px}
.welcome-logo .brand-name{font-size:18px;line-height:22px;width:150px}
.welcome-logo .brand-mark{width:26px;height:26px}
.welcome h2{left:378px;top:632px;font-size:17px;color:var(--white);font-weight:600;letter-spacing:-.3px}
.welcome p{left:378px;top:660px;width:310px;font-size:7.8px;line-height:13px;color:var(--text-light);letter-spacing:.15px}
.rule{left:101px;top:779px;width:588px;height:1px;background:linear-gradient(90deg,transparent,#333 20%,#333 80%,transparent)}

/* articles */
.article-image{left:101px;top:804px;width:252px;height:127px;border:3px solid #aaa;background:radial-gradient(circle at 50% 55%,#1d6fd6 0%,#0d3070 35%,#030a1a 70%,#000 100%)}
.articles h2{left:102px;top:935px;font-size:22px;line-height:24px;color:var(--white);font-weight:500}
.article-list{left:102px;top:988px;list-style:none}
.article-list li{font-size:8px;color:var(--white);line-height:15.3px}
.article-list li::before{content:"→";color:var(--yellow);margin-right:7px}
.divider-v{left:376px;top:804px;width:1px;height:258px;background:#2a2a2a}

.feature{position:absolute;width:140px}
.feature h3{display:flex;align-items:center;gap:5px;font-size:14px;color:var(--white);font-weight:500;height:20px;letter-spacing:-.4px}
.feature h3 svg{flex:none}
.feature p{font-size:8px;line-height:10.6px;color:var(--white);margin-top:9px;height:58px}
.feature ul{list-style:none;margin-top:9px;height:58px}
.feature li{font-size:8px;color:var(--white);line-height:17.5px}
.feature li::before{content:"→";color:var(--yellow);margin-right:7px}
.p-wide{letter-spacing:1.6px}

/* footer */
.site-footer{position:absolute;left:0;top:1080px;width:790px;height:120px;background:var(--grey-footer);border-top:4px solid var(--yellow)}
.foot-brand{left:112px;top:1097px;width:140px;display:flex;align-items:center;gap:6px}
.foot-brand .brand-name{color:#bbb;font-size:10.5px;line-height:13px}
.foot-brand .brand-mark{width:16px;height:16px}
.copyright{left:122px;top:1158px;font-size:7px;color:#ddd}
.follow{left:119px;top:1179px;font-size:10px;color:#ddd;display:flex;align-items:center;gap:3px}
.follow i{width:11px;height:11px;border-radius:50%;background:#eee;display:inline-block}
.foot-col h4{font-size:11px;font-weight:600;color:var(--white);padding-bottom:5px;border-bottom:1px dotted #666;width:94px}
.foot-col ul{list-style:none;margin-top:4px}
.foot-col li{font-size:7.8px;color:#ddd;line-height:15.7px}
.foot-col li::before{content:"›";margin-right:5px;color:#999}
.contact-row{display:flex;gap:6px;font-size:7.6px;color:#ddd;line-height:11.5px;margin-top:8px}
.inquiry input,.inquiry textarea{display:block;width:123px;background:var(--white);border:0;font:7px 'Open Sans',sans-serif;color:#999;padding:2px 5px;margin-bottom:3px;height:14px}
.inquiry textarea{height:24px;resize:none}
.submit{float:right;background:var(--yellow);font-size:7.5px;font-weight:700;color:var(--ink);line-height:12px;padding:0 7px;margin-right:-14px}
</style>
</head>
<body>

<header class="site-header">
  <div class="brand"><span class="brand-mark"></span><span class="brand-name">Brightlane Pixel Collective</span></div>
  <div class="phones"><b>TOLL FREE :</b> <span>1-877-512-3081</span><b>Local :</b> <span style="margin:0">612-555-0148</span></div>
  <nav class="main-nav">
    <span class="nav-home"><svg width="16" height="14" viewBox="0 0 16 14"><path d="M8 1 1 7h2v6h4V9h2v4h4V7h2z" fill="none" stroke="#000" stroke-width="1.6"/></svg></span>
    <a>Web Design</a><a>Search Engine Marketing</a><a>Social Media</a><a>Contact Us</a>
  </nav>
</header>

<section class="hero" role="img" aria-label="Photo of a hand touching floating words about SEO, media, technology and social marketing"></section>
<div class="slider-dots"><i></i><i></i><i class="on"></i></div>

<section class="services">
  <div class="service" style="left:91px">
    <div class="svc-icon active"><svg width="44" height="44" viewBox="0 0 44 44" fill="none" stroke="#fff" stroke-width="3.5"><circle cx="18" cy="18" r="12"/><path d="M27 27l11 11" stroke-linecap="round"/><circle cx="18" cy="16" r="4" stroke-width="2.5"/><path d="M18 20v5" stroke-width="2.5"/></svg></div>
    <h3 class="heading">Sarch Engine Market</h3>
    <p>When a person goes online to search for a specific product or service they are typically in the buying phase...<br>If you are not AT THE TOP</p>
    <span class="btn-dark">MORE</span>
  </div>
  <div class="service" style="left:243px">
    <div class="svc-icon"><svg width="46" height="40" viewBox="0 0 46 40" fill="none" stroke="#fff" stroke-width="3"><rect x="3" y="5" width="40" height="26" rx="2"/><path d="M18 38h10M23 31v7"/><path d="M15 25l4-1 15-15-3-3-15 15z" fill="#fff" stroke-width="1.5"/></svg></div>
    <h3 class="heading">Web Design</h3>
    <p>Welcome to Brightlane Pixel. We are very excited and proud to help you achieve the internet solution that you need. We have an experienced.</p>
    <span class="btn-dark">MORE</span>
  </div>
  <div class="service" style="left:394px">
    <div class="svc-icon"><svg width="50" height="50" viewBox="0 0 50 50" fill="none" stroke="#fff" stroke-width="2"><circle cx="25" cy="25" r="7"/><circle cx="16" cy="8" r="5"/><circle cx="34" cy="8" r="5"/><circle cx="7" cy="27" r="5"/><circle cx="43" cy="27" r="5"/><circle cx="25" cy="44" r="5"/><path d="M19 12l3 6M31 12l-3 6M12 27h6M38 27h-6M25 32v7"/></svg></div>
    <h3 class="heading">Social Media</h3>
    <p>Social Networking is the fastest growing and most cost effective marketing platform today. If you don't already understand the #1 reason why your business</p>
    <span class="btn-dark">MORE</span>
  </div>
  <div class="service" style="left:545px">
    <div class="svc-icon"><svg width="46" height="44" viewBox="0 0 46 44" fill="none" stroke="#fff" stroke-width="3"><rect x="4" y="10" width="32" height="28" rx="2"/><path d="M10 16v16"/><path d="M18 30l3-8 17-17 5 5-17 17z" fill="#2b2b2b" stroke-width="2.5"/></svg></div>
    <h3 class="heading">Graphic Design</h3>
    <p>You've invested countless hours and a large sum of money to build your online presence, why waste the investment by not marketing it?</p>
    <span class="btn-dark">MORE</span>
  </div>
</section>

<section class="welcome">
  <div class="abs welcome-logo"><span class="brand-mark"></span><span class="brand-name">Brightlane Pixel Collective</span></div>
  <h2 class="abs heading">Welcome to Brightlane Pixel Collective</h2>
  <p class="abs">We are an award winning web design &amp; internet marketing company located in Minneapolis. As a Minneapolis Web Design company, we create web sites to what our clients want and that's found in our marketing. Here at Brightlane Pixel Collective, we not only design you a first class web presence but market your website so your buyer finds you first before anyone else. A great web presence is built from a client's ideas and the innovative imagination of our Minneapolis Web Designer base and the skills of our internet marketing team.</p>
  <div class="abs rule"></div>
</section>

<section class="articles">
  <div class="abs article-image" role="img" aria-label="Illustration of glowing blue 3D lettering reading web design"></div>
  <h2 class="abs heading">Top Articles Web Design<br>Minneapolis</h2>
  <ul class="abs article-list">
    <li>Converting Social Media Traffic into Sales</li>
    <li>How much does online marketing cost?</li>
    <li>How to develop a website marketing strategy</li>
  </ul>
  <span class="abs btn-yellow" style="left:101px;top:1037px">More</span>
  <div class="abs divider-v"></div>

  <div class="feature" style="left:401px;top:804px">
    <h3 class="heading"><svg width="18" height="18" viewBox="0 0 18 18" fill="none" stroke="#fbb829" stroke-width="2"><circle cx="8" cy="10" r="6.5"/><circle cx="8" cy="10" r="3"/><path d="M8 10l8-8M13 2h3v3"/></svg>Our Mission</h3>
    <p><span>We are an award winning web design &amp; internet marketing</span> <span class="p-wide">company located in</span> Minneapolis. As a Minneapolis Web Design company.</p>
    <span class="btn-yellow">More</span>
  </div>
  <div class="feature" style="left:547px;top:804px">
    <h3 class="heading"><svg width="18" height="15" viewBox="0 0 18 15"><rect x="0" y="3" width="18" height="12" rx="1" fill="#fbb829"/><rect x="6" y="0" width="6" height="4" fill="none" stroke="#fbb829" stroke-width="1.5"/><rect x="0" y="8" width="18" height="1" fill="#000"/></svg>Internet Marketing</h3>
    <p>You've invested countless hours and a large sum of money to build your online presence, why waste the investment by not marketing it?</p>
    <span class="btn-yellow">More</span>
  </div>
  <div class="feature" style="left:401px;top:944px">
    <h3 class="heading"><svg width="18" height="14" viewBox="0 0 18 14"><path d="M0 1h6l2 2h10v11H0z" fill="#fbb829"/></svg>Development</h3>
    <ul><li>Lorem ipsum dolor sit amet</li><li>Lorem ipsum dolor sit amet</li><li>Lorem ipsum dolor sit amet</li></ul>
    <span class="btn-yellow">More</span>
  </div>
  <div class="feature" style="left:547px;top:944px">
    <h3 class="heading"><svg width="18" height="15" viewBox="0 0 18 15" fill="none" stroke="#fbb829" stroke-width="1.6"><rect x="1" y="2" width="15" height="10"/><path d="M6 14h5"/><path d="M6 9l2-.5 8-8" stroke-width="2"/></svg>Webdesign</h3>
    <p>Welcome to Brightlane Pixel. We are very excited and proud to help you achieve the internet solution that you need. We have an experienced team.</p>
    <span class="btn-yellow">More</span>
  </div>
</section>

<footer class="site-footer"></footer>
<div class="abs foot-brand"><span class="brand-mark"></span><span class="brand-name">Brightlane Pixel Collective</span></div>
<div class="abs copyright">@ 2014 | PRIVACY POLICY</div>
<div class="abs follow">Follow Us : <i></i><i></i><i></i></div>

<div class="abs foot-col" style="left:258px;top:1095px">
  <h4>Quick Links</h4>
  <ul><li>Home</li><li>Web Design</li><li>Search Engine Marketing</li><li>Social Media</li><li>Contact Us</li></ul>
</div>
<div class="abs foot-col" style="left:397px;top:1095px">
  <h4>Contact Details</h4>
  <div class="contact-row"><svg width="7" height="10" viewBox="0 0 7 10"><path d="M3.5 0A3.5 3.5 0 0 0 0 3.5C0 6 3.5 10 3.5 10S7 6 7 3.5A3.5 3.5 0 0 0 3.5 0z" fill="#bbb"/><circle cx="3.5" cy="3.5" r="1.3" fill="#3d3d3d"/></svg><span>Lorem ipsum dolor sit amet<br>consectetuer adipiscing elit<br>sed diam nonummy.</span></div>
  <div class="contact-row"><svg width="8" height="8" viewBox="0 0 8 8"><path d="M1 0l2 2-1 1.3c.6 1.2 1.5 2.1 2.7 2.7L6 5l2 2-1 1C3.5 8 0 4.5 0 1z" fill="#bbb"/></svg><span>123-456-7890</span></div>
  <div class="contact-row"><svg width="9" height="7" viewBox="0 0 9 7"><rect width="9" height="7" fill="#bbb"/><path d="M0 0l4.5 4L9 0" fill="none" stroke="#3d3d3d"/></svg><span>info@brightlanepixelcollective.com</span></div>
</div>
<div class="abs foot-col inquiry" style="left:553px;top:1095px">
  <h4 style="border:0">Quick Inquiry</h4>
  <input placeholder="Name" style="margin-top:2px">
  <input placeholder="Email">
  <textarea placeholder="Message"></textarea>
  <span class="submit">SUBMIT</span>
</div>

</body>
</html>
```